Email Signature Gif Animation Design

We are looking for an interactive Email Signature to Standardize around for our growing company.

We are a commerical electrical contractor based out of North Jersey. We have a big corporate client tele and perfer a more professional fresh looking signature with titles and perhaps a suttle animation for effect.

Attached below is our company logo which is to be used prominently in the emai signature. We would consider a "refresh' of our logo design provided it does deviate too much.

We would like the tag Line "The KALV Electric Way" worked into that signature as a option.
Updates

Reviewing designs and am underwhelmed with the creativiity and designs, this is anyones prize!

Target Market(s)

Corporate / Middle Managers

Industry/Entity Type

Electrical Contracting & Engineering

Colors
FFF300
FFF600
FEFA6F
FFFEC7
FFFEE8

Requirements
Must have
• Must have, First & Last Name of Employee, Title of Employee, Office & Cell Phone Number, Email Address
Nice to have
• Gif Animation

```html
<!DOCTYPE html>
<html lang="en">
<head>
<meta charset="utf-8">
<title>KALV Electric – Email Signature</title>
<link href="https://fonts.googleapis.com/css2?family=Oswald:wght@500;700&family=Open+Sans:ital,wght@0,400;1,400&display=swap" rel="stylesheet">
<style>
  :root {
    --stage: #505050;
    --paper: #ffffff;
    --ink: #0d0d0d;
    --gold: #d9b31f;
    --rule: #6a6a6a;
    --halftone: #d8d8d8;
  }
  * { margin: 0; padding: 0; box-sizing: border-box; }
  html, body { width: 1200px; height: 641px; overflow: hidden; background: var(--stage); }
  .signature {
    position: absolute; left: 87px; top: 199px;
    width: 1027px; height: 243px;
    background: var(--paper); overflow: hidden;
    font-family: "Open Sans", Arial, sans-serif; color: var(--ink);
  }
  .texture {
    position: absolute; left: 0; top: 0; width: 330px; height: 222px;
    background: radial-gradient(ellipse at 0% 0%, var(--halftone) 0%, rgba(255,255,255,0) 70%);
  }
  .tagline {
    position: absolute; right: 0; top: 0; width: 352px; height: 43px;
    background: var(--gold);
    clip-path: polygon(0 0, 100% 0, 100% 100%, 24px 100%);
    font-family: "Oswald", Arial, sans-serif; font-weight: 700;
    font-size: 30px; line-height: 43px; letter-spacing: 1.5px;
    text-align: right; padding-right: 16px; color: var(--ink);
  }
  .brand {
    position: absolute; left: 73px; top: 118px; width: 187px;
    display: flex; align-items: center; gap: 9px;
  }
  .brand-square { width: 22px; height: 22px; background: var(--gold); flex: none; }
  .brand-name {
    font-family: "Oswald", Arial, sans-serif; font-weight: 700;
    font-size: 22px; letter-spacing: 1px; color: var(--ink); line-height: 1;
    white-space: nowrap;
  }
  .person { position: absolute; left: 297px; top: 90px; width: 270px; }
  .person-name {
    font-family: "Oswald", Arial, sans-serif; font-weight: 700;
    font-size: 40px; letter-spacing: 2px; line-height: 1.1; white-space: nowrap;
  }
  .person-title { font-style: italic; font-size: 21px; margin-top: 14px; white-space: nowrap; }
  .divider {
    position: absolute; left: 589px; top: 77px; width: 3px; height: 120px;
    background: var(--gold); border-radius: 2px;
  }
  .contacts { position: absolute; left: 628px; top: 0; }
  .contact-icon { position: absolute; left: 0; }
  .contact-text {
    position: absolute; left: 46px; white-space: nowrap;
    font-size: 20px; line-height: 1;
  }
  .contact-text small { font-size: 9px; }
  .footer-band {
    position: absolute; left: 0; bottom: 0; width: 528px; height: 22px;
    background: var(--ink); clip-path: polygon(0 0, 518px 0, 100% 100%, 0 100%);
  }
  .footer-rule {
    position: absolute; left: 528px; top: 239px; width: 324px; height: 1px;
    background: var(--rule);
  }
  .footer-brand {
    position: absolute; left: 855px; top: 222px; width: 160px;
    font-family: "Oswald", Arial, sans-serif; font-weight: 700; color: var(--ink);
    text-align: center; line-height: 1;
  }
  .footer-brand .line-main { font-size: 12px; letter-spacing: 1px; }
  .footer-brand .line-sub { font-size: 6px; letter-spacing: 2.6px; margin-top: 2px; }
</style>
</head>
<body>
  <div class="signature">
    <div class="texture" role="img" aria-label="Soft halftone dot texture"></div>

    <div class="tagline">The KALV Electric Way</div>

    <div class="brand">
      <span class="brand-square"></span>
      <span class="brand-name">KALV ELECTRIC</span>
    </div>

    <div class="person">
      <div class="person-name">DANIEL REYES</div>
      <div class="person-title">Marketing Manager</div>
    </div>

    <div class="divider"></div>

    <div class="contacts">
      <svg class="contact-icon" style="top:74px" width="30" height="30" viewBox="0 0 30 30">
        <circle cx="15" cy="15" r="15" fill="#0d0d0d"/>
        <rect x="8" y="10" width="14" height="10" fill="#d9b31f"/>
        <path d="M8 10 L15 16 L22 10" fill="none" stroke="#0d0d0d" stroke-width="1.2"/>
      </svg>
      <div class="contact-text" style="top:78px">name@thecompany.com</div>

      <svg class="contact-icon" style="top:117px" width="30" height="30" viewBox="0 0 30 30">
        <circle cx="15" cy="15" r="15" fill="#0d0d0d"/>
        <g fill="none" stroke="#d9b31f" stroke-width="1.3">
          <circle cx="15" cy="15" r="8"/>
          <ellipse cx="15" cy="15" rx="3.5" ry="8"/>
          <line x1="7" y1="15" x2="23" y2="15"/>
          <line x1="8.5" y1="11" x2="21.5" y2="11"/>
          <line x1="8.5" y1="19" x2="21.5" y2="19"/>
        </g>
      </svg>
      <div class="contact-text" style="top:119px">yourwebaddress.com</div>

      <svg class="contact-icon" style="top:161px" width="30" height="30" viewBox="0 0 30 30">
        <circle cx="15" cy="15" r="15" fill="#0d0d0d"/>
        <path d="M10.5 8.5 l3 0 l1 4 l-2 1.3 a9 9 0 0 0 3.7 3.7 l1.3 -2 l4 1 l0 3 a2 2 0 0 1 -2 2 a12 12 0 0 1 -11 -11 a2 2 0 0 1 2 -2 z" fill="#d9b31f"/>
      </svg>
      <div class="contact-text" style="top:155px">123 456 7890 <small>(Home)</small></div>
      <div class="contact-text" style="top:183px">123 456 7890 <small>(Office)</small></div>
    </div>

    <div class="footer-band"></div>
    <div class="footer-rule"></div>
    <div class="footer-brand">
      <div class="line-main">KALV ELECTRIC LLC</div>
      <div class="line-sub">ELECTRICAL CONTRACTORS</div>
    </div>
  </div>
</body>
</html>
```